Velora Aesthetica

Medical doctor providing aesthetic medicine

* Double sided card
* Logo to be on card
Other details:
* Dr. Mirela Kostvan, BSc, MBChB, CCFP
* #214-215, 27903 83 Ave, Surrey, BC, V2T 4K7
* 604-718-2943
* info@veloraclinic.ca
* www.veloraclinic.ca

Industry/Entity Type

Medical / Health & Beauty

Contact Information for Business Card

see 'Project Description'

Colors
0054AA
0677BA
7BADD7
CADEEF
E8F1F8
FFF300
FFF600
FEFA6F
FFFEC7
FFFEE8

Requirements
Must have
• Modern, high-end design

```html
<!DOCTYPE html>
<html lang="en">
<head>
<meta charset="utf-8">
<title>Velora Aesthetica — Business Card</title>
<link rel="stylesheet" href="https://fonts.googleapis.com/css2?family=Montserrat:wght@500;600&family=Poppins:wght@400;600&display=swap">
<style>
  :root {
    --backdrop: #ece9e4;
    --card-white: #ffffff;
    --ink: #161616;
    --gold: #c9a227;
    --gold-light: #e6c02e;
    --gold-deep: #a98519;
    --navy: #17174e;
    --rule: #3a3a3a;
    --white: #ffffff;
  }
  * { box-sizing: border-box; margin: 0; padding: 0; }
  html, body {
    width: 900px; height: 1200px; overflow: hidden;
    background: var(--backdrop);
  }
  .canvas { position: relative; width: 900px; height: 1200px; }

  .card {
    position: absolute;
    border-radius: 32px;
    overflow: hidden;
    box-shadow: 0 6px 14px rgba(0,0,0,0.18);
  }

  /* Front */
  .card-front {
    left: 73px; top: 113px; width: 760px; height: 447px;
    background: var(--card-white);
    font-family: "Poppins", sans-serif;
    color: var(--ink);
  }
  .doctor-name {
    position: absolute; left: 40px; top: 48px;
    font-weight: 600; font-size: 31px; letter-spacing: 0.2px;
    line-height: 1;
  }
  .credentials {
    position: absolute; left: 40px; top: 91px;
    font-size: 20px; color: var(--gold); line-height: 1;
  }
  .brand-front {
    position: absolute; left: 440px; top: 40px; width: 300px;
    text-align: center;
  }
  .brand-dot {
    display: block; margin: 0 auto 22px;
    width: 120px; height: 120px; border-radius: 50%;
    border: 3px solid var(--gold);
  }
  .brand-name {
    font-family: "Montserrat", sans-serif;
    font-weight: 500;
    text-transform: uppercase;
    letter-spacing: 6px;
    line-height: 1.2;
  }
  .brand-front .brand-name { font-size: 26px; color: var(--ink); }

  .contact-rule {
    position: absolute; left: 40px; top: 311px; width: 680px;
    height: 1px; background: var(--rule);
  }
  .contact-list {
    position: absolute; left: 40px; top: 322px;
    list-style: none; font-size: 17px; line-height: 27px;
  }
  .contact-list li { display: flex; align-items: center; gap: 10px; }
  .contact-list svg { width: 17px; height: 17px; fill: var(--gold); flex: none; }
  .address {
    position: absolute; right: 38px; top: 322px;
    font-size: 17px; line-height: 27px;
  }
  .gold-band {
    position: absolute; left: 0; bottom: 0; width: 100%; height: 20px;
    background: linear-gradient(90deg, var(--gold-deep), var(--gold-light) 55%, var(--gold));
  }

  /* Back */
  .card-back {
    left: 67px; top: 640px; width: 763px; height: 445px;
    background: var(--navy);
    text-align: center;
  }
  .brand-back { position: absolute; left: 0; top: 115px; width: 100%; }
  .brand-back .brand-dot { width: 140px; height: 140px; margin-bottom: 26px; }
  .brand-back .brand-name { font-size: 30px; color: var(--white); letter-spacing: 8px; }
  .website-back {
    position: absolute; left: 0; top: 391px; width: 100%;
    font-family: "Montserrat", sans-serif; font-weight: 500;
    font-size: 17px; letter-spacing: 4px; color: var(--white);
    text-transform: uppercase;
  }
</style>
</head>
<body>
<main class="canvas">

  <section class="card card-front" aria-label="Card front">
    <h1 class="doctor-name">DR. MIRELA KOSTVAN</h1>
    <p class="credentials">BSc, MBChB, CCFP</p>

    <div class="brand-front">
      <span class="brand-dot" aria-hidden="true"></span>
      <p class="brand-name">Velora<br>Aesthetica</p>
    </div>

    <div class="contact-rule"></div>
    <ul class="contact-list">
      <li>
        <svg viewBox="0 0 24 24" aria-hidden="true"><path d="M6.6 10.8a15.2 15.2 0 0 0 6.6 6.6l2.2-2.2a1 1 0 0 1 1-.25 11.4 11.4 0 0 0 3.6.57 1 1 0 0 1 1 1V20a1 1 0 0 1-1 1A17 17 0 0 1 3 4a1 1 0 0 1 1-1h3.5a1 1 0 0 1 1 1c0 1.25.2 2.45.57 3.6a1 1 0 0 1-.25 1z"/></svg>
        604-718-2943
      </li>
      <li>
        <svg viewBox="0 0 24 24" aria-hidden="true"><path d="M2 5h20v14H2z M2 6l10 7 10-7" fill="var(--gold)"/><path d="M2.5 5.5l9.5 6.8 9.5-6.8" stroke="#fff" stroke-width="1.6" fill="none"/></svg>
        info@veloraclinic.ca
      </li>
      <li>
        <svg viewBox="0 0 24 24" aria-hidden="true"><circle cx="12" cy="12" r="10"/><path d="M2 12h20M12 2c3 3 3 17 0 20M12 2c-3 3-3 17 0 20M4 7h16M4 17h16" stroke="#fff" stroke-width="1.3" fill="none"/></svg>
        www.veloraclinic.ca
      </li>
    </ul>
    <p class="address">#214-215, 27903 83 Ave, Surrey, BC, V2T 4K7</p>

    <div class="gold-band"></div>
  </section>

  <section class="card card-back" aria-label="Card back">
    <div class="brand-back">
      <span class="brand-dot" aria-hidden="true"></span>
      <p class="brand-name">Velora Aesthetica</p>
    </div>
    <p class="website-back">www.veloraclinic.ca</p>
  </section>

</main>
</body>
</html>
```